Brenton Wealth Management Flow Charts

I need help creating three flow charts for my businesses website. We want them to be simple but look professional. This is for a Wealth Management firm. I will attach a word document that has all of the descriptions for everything so you know what icons to use. We just want the chart to have an icon, the names of each step and the corresponding numbers. I will also include some examples of charts we liked as well. Once the winner is selected, we will need help with additional graphic design elements for our website ASAP.
- Goudy Roman

```html
<!DOCTYPE html>
<html lang="en">
<head>
<meta charset="utf-8">
<title>Wealth Planning Process Charts</title>
<link href="https://fonts.googleapis.com/css2?family=Montserrat:wght@400;500;600;700&display=swap" rel="stylesheet">
<style>
  :root{
    --ink:#5a5a5a;
    --muted:#8a8a8a;
    --rule:#e9e9e9;
    --box-line:#9b9b9b;
    --r1:#1d2f7a; --r2:#244c9c; --r3:#2a6fb0; --r4:#2c8bb4; --r5:#2fa8bc; --r6:#4ccfc6;
    --i1:#e8365c; --i2:#f07a2a; --i3:#8db53b; --i4:#3f9a86; --i5:#2a9fd8; --i6:#7b4aa8;
    --l1:#2ab5c8; --l2:#7a5aa8; --l3:#4fa64a; --l4:#f08a2a; --l5:#8db53b;
  }
  html,body{margin:0;padding:0;width:1200px;height:2316px;overflow:hidden;background:#fff}
  svg{display:block;font-family:"Montserrat",Arial,sans-serif}
  .step-label{font-size:18px;fill:var(--ink);font-weight:500;letter-spacing:.5px}
  .step-label--caps{text-transform:uppercase;font-size:17px;letter-spacing:1px}
  .step-num{font-size:44px;font-weight:700}
  .hub-title{font-size:16px;font-weight:600;fill:var(--muted);letter-spacing:1px}
  .hub-title--mixed{font-size:18px;fill:var(--ink);letter-spacing:0}
  .seg{stroke:#fff;stroke-width:6}
  .icon{fill:none;stroke:#fff;stroke-width:3;stroke-linecap:round;stroke-linejoin:round}
  .band{fill:var(--rule)}
  .band-title{font-size:21px;fill:var(--ink);font-weight:500}
  .legacy-box{fill:#fff;stroke:var(--box-line);stroke-width:2}
  .legacy-link{stroke:var(--box-line);stroke-width:2}
  .legacy-dots{stroke:var(--muted);stroke-width:3;stroke-dasharray:2 7;stroke-linecap:round}
  .legacy-label{font-size:19px;fill:var(--ink);font-weight:500}
  .pin-num{font-size:30px;font-weight:700}
</style>
</head>
<body>
<svg width="1200" height="2316" viewBox="0 0 1200 2316" xmlns="http://www.w3.org/2000/svg">

  <!-- Retirement planning process -->
  <g class="chart chart--retirement">
    <path class="seg" style="fill:var(--r1)" d="M600 130 A270 270 0 0 1 833.8 265 L699.6 342.5 A115 115 0 0 0 600 285Z"/>
    <path class="seg" style="fill:var(--r2)" d="M833.8 265 A270 270 0 0 1 833.8 535 L699.6 457.5 A115 115 0 0 0 699.6 342.5Z"/>
    <path class="seg" style="fill:var(--r3)" d="M833.8 535 A270 270 0 0 1 600 670 L600 515 A115 115 0 0 0 699.6 457.5Z"/>
    <path class="seg" style="fill:var(--r4)" d="M600 670 A270 270 0 0 1 366.2 535 L500.4 457.5 A115 115 0 0 0 600 515Z"/>
    <path class="seg" style="fill:var(--r5)" d="M366.2 535 A270 270 0 0 1 366.2 265 L500.4 342.5 A115 115 0 0 0 500.4 457.5Z"/>
    <path class="seg" style="fill:var(--r6)" d="M366.2 265 A270 270 0 0 1 600 130 L600 285 A115 115 0 0 0 500.4 342.5Z"/>
    <circle cx="600" cy="400" r="112" fill="#fff"/>
    <text class="hub-title" text-anchor="middle"><tspan x="600" y="380">THE</tspan><tspan x="600" y="404">RETIREMENT</tspan><tspan x="600" y="428">PLANNING PROCESS</tspan></text>

    <g class="icon" transform="translate(696 234)"><circle cx="-9" cy="-8" r="6"/><circle cx="9" cy="-8" r="6"/><path d="M-20 14 v-6 a9 9 0 0 1 18 0 v6 M2 14 v-6 a9 9 0 0 1 18 0 v6"/><path d="M-24 16 h48"/></g>
    <g class="icon" transform="translate(792 400)"><circle r="20"/><circle cy="-6" r="6"/><path d="M-10 12 a10 10 0 0 1 20 0"/></g>
    <g class="icon" transform="translate(696 566)"><rect x="-14" y="-18" width="28" height="36" rx="3"/><path d="M-7 -6 h14 M-7 2 h14 M-7 10 h8"/></g>
    <g class="icon" transform="translate(504 566)"><circle r="18"/><path d="M0 -10 v20 M5 -6 h-7 a3.5 3.5 0 0 0 0 7 h4 a3.5 3.5 0 0 1 0 7 h-7"/></g>
    <g class="icon" transform="translate(408 400)"><path d="M0 -18 v34 M-10 16 h20 M-18 -10 h36 M-18 -10 l-7 14 h14z M18 -10 l-7 14 h14z"/></g>
    <g class="icon" transform="translate(504 234)"><rect x="-15" y="-18" width="24" height="32" rx="3"/><circle cx="6" cy="6" r="8"/><path d="M12 12 l7 7"/></g>

    <text class="step-num" x="760" y="134" style="fill:var(--r1)">1</text>
    <text class="step-label step-label--caps" x="794" y="126">Discovery Meeting</text>
    <text class="step-num" x="922" y="420" style="fill:var(--r2)">2</text>
    <text class="step-label step-label--caps" x="956" y="412">Learning</text>
    <text class="step-num" x="760" y="718" style="fill:var(--r3)">3</text>
    <text class="step-label step-label--caps" x="794" y="710">Planning</text>
    <text class="step-label step-label--caps" x="400" y="710" text-anchor="end">Execution</text>
    <text class="step-num" x="408" y="718" style="fill:var(--r4)">4</text>
    <text class="step-label step-label--caps" x="244" y="412" text-anchor="end">Alignment</text>
    <text class="step-num" x="252" y="420" style="fill:var(--r5)">5</text>
    <text class="step-label step-label--caps" x="404" y="126" text-anchor="end">Review</text>
    <text class="step-num" x="412" y="134" style="fill:var(--r6)">6</text>
  </g>

  <!-- Comprehensive investment management -->
  <g class="chart chart--investment">
    <path class="seg" style="fill:var(--i1)" d="M600 920 A270 270 0 0 1 833.8 1055 L702.2 1131 A118 118 0 0 0 600 1072Z"/>
    <path class="seg" style="fill:var(--i2)" d="M833.8 1055 A270 270 0 0 1 833.8 1325 L702.2 1249 A118 118 0 0 0 702.2 1131Z"/>
    <path class="seg" style="fill:var(--i3)" d="M833.8 1325 A270 270 0 0 1 600 1460 L600 1308 A118 118 0 0 0 702.2 1249Z"/>
    <path class="seg" style="fill:var(--i4)" d="M600 1460 A270 270 0 0 1 366.2 1325 L497.8 1249 A118 118 0 0 0 600 1308Z"/>
    <path class="seg" style="fill:var(--i5)" d="M366.2 1325 A270 270 0 0 1 366.2 1055 L497.8 1131 A118 118 0 0 0 497.8 1249Z"/>
    <path class="seg" style="fill:var(--i6)" d="M366.2 1055 A270 270 0 0 1 600 920 L600 1072 A118 118 0 0 0 497.8 1131Z"/>
    <circle cx="600" cy="1190" r="114" fill="#fff" stroke="#e2e2e2" stroke-width="5"/>
    <text class="hub-title hub-title--mixed" text-anchor="middle"><tspan x="600" y="1170">Comprehensive</tspan><tspan x="600" y="1195">Investment</tspan><tspan x="600" y="1220">Management</tspan></text>

    <g class="icon" transform="translate(697 1026)"><path d="M-18 8 a18 18 0 0 1 36 0"/><path d="M0 8 l8 -12"/><path d="M0 -18 v-4"/></g>
    <g class="icon" transform="translate(795 1190)"><circle r="18"/><path d="M5 -7 h-7 a3.5 3.5 0 0 0 0 7 h4 a3.5 3.5 0 0 1 0 7 h-7 M0 -11 v22"/></g>
    <g class="icon" transform="translate(697 1354)"><circle r="18"/><path d="M0 0 V-18 M0 0 L16 8"/></g>
    <g class="icon" transform="translate(503 1354)"><path d="M-20 6 l12 -12 l10 8 l18 -14"/><path d="M12 -12 h8 v8"/></g>
    <g class="icon" transform="translate(405 1190)"><circle cy="-12" r="6"/><path d="M-16 16 v-6 a10 10 0 0 1 10 -10 h12 a10 10 0 0 1 10 10 v6"/></g>
    <g class="icon" transform="translate(503 1026)"><circle cy="-12" r="6"/><circle cx="-16" cy="8" r="5"/><circle cx="16" cy="8" r="5"/><path d="M0 -6 v8 M-16 2 v-4 h32 v4"/></g>

    <text class="step-num" x="760" y="920" style="fill:var(--i1)">1</text>
    <text class="step-label" x="794" y="900"><tspan>Understanding your Risk</tspan><tspan x="794" dy="23">Tolerance</tspan></text>
    <text class="step-num" x="906" y="1206" style="fill:var(--i2)">2</text>
    <text class="step-label" x="940" y="1186"><tspan>Investment</tspan><tspan x="940" dy="23">Selection</tspan></text>
    <text class="step-num" x="744" y="1500" style="fill:var(--i3)">3</text>
    <text class="step-label" x="778" y="1492">Asset Allocation</text>
    <text class="step-label" x="404" y="1492" text-anchor="end">Tax efficiency</text>
    <text class="step-num" x="412" y="1500" style="fill:var(--i4)">4</text>
    <text class="step-label" x="250" y="1186" text-anchor="end"><tspan>Distribution</tspan><tspan x="250" dy="23">Strategy</tspan></text>
    <text class="step-num" x="258" y="1206" style="fill:var(--i5)">5</text>
    <text class="step-label" x="408" y="900" text-anchor="end"><tspan>Behavior Finance</tspan><tspan x="408" dy="23">Coaching</tspan></text>
    <text class="step-num" x="416" y="920" style="fill:var(--i6)">6</text>
  </g>

  <!-- Legacy and estate planning -->
  <g class="chart chart--legacy">
    <rect class="band" x="80" y="1656" width="1040" height="46" rx="23"/>
    <text class="band-title" x="600" y="1686" text-anchor="middle">Legacy and Estate Planning</text>

    <g class="legacy-links">
      <line class="legacy-link" x1="256" y1="1962" x2="296" y2="1962"/>
      <line class="legacy-link" x1="472" y1="1962" x2="512" y2="1962"/>
      <line class="legacy-link" x1="688" y1="1962" x2="728" y2="1962"/>
      <line class="legacy-link" x1="904" y1="1962" x2="944" y2="1962"/>
    </g>

    <g transform="translate(168 20)">
      <path d="M-34 1770 a34 34 0 1 1 68 0 a34 34 0 0 1 -22 32 l-12 14 l-12 -14 a34 34 0 0 1 -22 -32z" style="fill:var(--l1)"/>
      <circle cy="1770" r="25" fill="#fff"/>
      <text class="pin-num" y="1781" text-anchor="middle" style="fill:var(--l1)">1</text>
      <line class="legacy-dots" x1="0" y1="1828" x2="0" y2="1864"/>
      <rect class="legacy-box" x="-88" y="1872" width="176" height="140" rx="18"/>
      <g style="fill:var(--r3)"><circle cy="1914" r="9"/><rect x="-11" y="1925" width="22" height="10" rx="4"/><rect x="-2" y="1935" width="4" height="8"/><rect x="-34" y="1943" width="68" height="4"/><rect x="-34" y="1943" width="4" height="8"/><rect x="30" y="1943" width="4" height="8"/><rect x="-2" y="1943" width="4" height="8"/>
        <circle cx="-32" cy="1958" r="6"/><circle cy="1958" r="6"/><circle cx="32" cy="1958" r="6"/><rect x="-40" y="1965" width="16" height="9" rx="3"/><rect x="-8" y="1965" width="16" height="9" rx="3"/><rect x="24" y="1965" width="16" height="9" rx="3"/></g>
      <text class="legacy-label" y="2100" text-anchor="middle">Beneficiaries</text>
    </g>

    <g transform="translate(384 20)">
      <path d="M-34 1770 a34 34 0 1 1 68 0 a34 34 0 0 1 -22 32 l-12 14 l-12 -14 a34 34 0 0 1 -22 -32z" style="fill:var(--l2)"/>
      <circle cy="1770" r="25" fill="#fff"/>
      <text class="pin-num" y="1781" text-anchor="middle" style="fill:var(--l2)">2</text>
      <line class="legacy-dots" x1="0" y1="1828" x2="0" y2="1864"/>
      <rect class="legacy-box" x="-88" y="1872" width="176" height="140" rx="18"/>
      <g fill="none" stroke="var(--l2)" stroke-width="6" stroke-linecap="round" stroke-linejoin="round">
        <path d="M-40 1932 h14 l22 -10 l14 8"/><path d="M40 1932 h-14 l-18 16 l-12 -8"/><path d="M-26 1932 l24 24 l20 -10"/></g>
      <text class="legacy-label" y="2100" text-anchor="middle">Trusts</text>
    </g>

    <g transform="translate(600 20)">
      <path d="M-34 1770 a34 34 0 1 1 68 0 a34 34 0 0 1 -22 32 l-12 14 l-12 -14 a34 34 0 0 1 -22 -32z" style="fill:var(--l3)"/>
      <circle cy="1770" r="25" fill="#fff"/>
      <text class="pin-num" y="1781" text-anchor="middle" style="fill:var(--l3)">3</text>
      <line class="legacy-dots" x1="0" y1="1828" x2="0" y2="1864"/>
      <rect class="legacy-box" x="-88" y="1872" width="176" height="140" rx="18"/>
      <path d="M0 1908 l-38 32 h10 v30 h56 v-30 h10z" style="fill:var(--l3)"/>
      <text x="0" y="1964" text-anchor="middle" fill="#fff" font-size="24" font-weight="700">%</text>
      <text class="legacy-label" y="2088" text-anchor="middle"><tspan x="0">Estate Taxes and</tspan><tspan x="0" dy="25">Assessment</tspan></text>
    </g>

    <g transform="translate(816 20)">
      <path d="M-34 1770 a34 34 0 1 1 68 0 a34 34 0 0 1 -22 32 l-12 14 l-12 -14 a34 34 0 0 1 -22 -32z" style="fill:var(--l4)"/>
      <circle cy="1770" r="25" fill="#fff"/>
      <text class="pin-num" y="1781" text-anchor="middle" style="fill:var(--l4)">4</text>
      <line class="legacy-dots" x1="0" y1="1828" x2="0" y2="1864"/>
      <rect class="legacy-box" x="-88" y="1872" width="176" height="140" rx="18"/>
      <path d="M6 1932 c-8 -10 -24 -2 -14 10 l14 12 l14 -12 c10 -12 -6 -20 -14 -10z" style="fill:var(--l4)"/>
      <path d="M-40 1952 h12 v22 h-12z M-26 1954 h14 l12 6 h14 l14 -8 l6 6 l-20 16 h-40z" style="fill:var(--l4)"/>
      <text class="legacy-label" y="2100" text-anchor="middle">Annual Giving</text>
    </g>

    <g transform="translate(1032 20)">
      <path d="M-34 1770 a34 34 0 1 1 68 0 a34 34 0 0 1 -22 32 l-12 14 l-12 -14 a34 34 0 0 1 -22 -32z" style="fill:var(--l5)"/>
      <circle cy="1770" r="25" fill="#fff"/>
      <text class="pin-num" y="1781" text-anchor="middle" style="fill:var(--l5)">5</text>
      <line class="legacy-dots" x1="0" y1="1828" x2="0" y2="1864"/>
      <rect class="legacy-box" x="-88" y="1872" width="176" height="140" rx="18"/>
      <g style="fill:var(--l5)"><rect x="-40" y="1934" width="40" height="8" rx="3"/><rect x="-40" y="1944" width="40" height="8" rx="3"/><rect x="-40" y="1954" width="40" height="8" rx="3"/><rect x="-40" y="1964" width="40" height="8" rx="3"/></g>
      <circle cx="16" cy="1946" r="22" style="fill:var(--l3)"/>
      <text x="16" y="1955" text-anchor="middle" fill="#fff" font-size="26" font-weight="700">$</text>
      <text class="legacy-label" y="2088" text-anchor="middle"><tspan x="0">Donations and</tspan><tspan x="0" dy="25">Charity</tspan></text>
    </g>
  </g>
</svg>
</body>
</html>
```